Dorans Greens

We require an A4 landscape leaflet with a fold down the middle, designed on all 4 sides to represent our home delivery fruit and vegetable box scheme. The leaflet should emphasize on our Free Trial Box offer (no commitment/obligation / £2 delivery charge applies / contents are 100% free) Offer applies to our small box only. We do a large box for £18.50, a medium box for £13 and a small box for £7.50. The leaflet should also show that we deliver extra products such as milk, artisan bread, meat boxes, fresh fish boxes, award winning sausage/pies etc
For more info on our service visit www.doransgreens.co.uk
Updates

Project Deadline Extended
Reason: Currently away so need more time to decide and apply changes required.

Industry/Entity Type

Landscape

```html
<!DOCTYPE html>
<html lang="en">
<head>
<meta charset="utf-8">
<title>Dorans Greens – Box Sizes</title>
<link rel="stylesheet" href="https://fonts.googleapis.com/css2?family=Germania+One&family=Open+Sans:wght@400;600&display=swap">
<style>
  :root {
    --stage-light: #f4f4f4;
    --stage-dark: #c9c9c9;
    --label-grey: #8a8a8a;
    --leaf-light: #b5d84a;
    --leaf-mid: #8fc43a;
    --forest: #1f3a1f;
    --gold: #f5c518;
    --tag-yellow: #fbbd1e;
    --badge-red: #e3262b;
    --ink: #1d2a12;
    --white: #ffffff;
  }
  html, body {
    margin: 0;
    padding: 0;
    width: 1200px;
    height: 1000px;
    overflow: hidden;
  }
  body {
    position: relative;
    background: radial-gradient(ellipse at 50% 20%, var(--stage-light) 0%, var(--stage-dark) 100%);
    font-family: "Open Sans", Arial, sans-serif;
  }
  .page-label {
    position: absolute;
    top: 72px;
    left: 0;
    width: 1200px;
    text-align: center;
    font-size: 44px;
    color: var(--label-grey);
    margin: 0;
    font-weight: 400;
  }
  .leaflet {
    position: absolute;
    top: 0;
    left: 0;
  }
  .display { font-family: "Germania One", Georgia, serif; }
  .body-copy { font-family: "Open Sans", Arial, sans-serif; }
</style>
</head>
<body>
  <p class="page-label">Page - 2</p>

  <svg class="leaflet" width="1200" height="1000" viewBox="0 0 1200 1000">
    <defs>
      <radialGradient id="panel-bg" cx="0.5" cy="0.45" r="0.7">
        <stop offset="0" stop-color="var(--leaf-light)"/>
        <stop offset="1" stop-color="var(--leaf-mid)"/>
      </radialGradient>
      <linearGradient id="produce-box" x1="0" y1="0" x2="0" y2="1">
        <stop offset="0" stop-color="#d94a2a"/>
        <stop offset="0.35" stop-color="#7c3f6e"/>
        <stop offset="0.5" stop-color="#c99a5c"/>
        <stop offset="1" stop-color="#a86a36"/>
      </linearGradient>
    </defs>

    <!-- panel -->
    <rect class="panel" x="88" y="206" width="1024" height="724" fill="url(#panel-bg)"/>

    <!-- header band -->
    <g class="header-band">
      <rect x="88" y="255" width="1024" height="83" fill="var(--forest)"/>
      <rect x="88" y="255" width="1024" height="3" fill="var(--gold)"/>
      <rect x="88" y="335" width="1024" height="3" fill="var(--gold)"/>
      <text class="display" x="600" y="313" text-anchor="middle" font-size="44" fill="var(--gold)" letter-spacing="2">Three Box Sizes To Choose From</text>
    </g>

    <!-- strings -->
    <g class="strings" fill="none" stroke="var(--forest)" stroke-width="3">
      <path d="M279,346 C268,400 292,440 280,480 C270,520 292,540 285,565"/>
      <path d="M551,346 C542,390 560,430 548,460 C540,490 556,500 551,512"/>
      <path d="M871,346 C862,365 880,380 868,395 C864,402 872,407 871,412"/>
    </g>

    <!-- grommets -->
    <g class="grommets" fill="var(--leaf-mid)" stroke="var(--gold)" stroke-width="4">
      <circle cx="279" cy="346" r="10"/>
      <circle cx="551" cy="346" r="10"/>
      <circle cx="871" cy="346" r="10"/>
    </g>

    <!-- price tags -->
    <g class="price-tag tag-small">
      <path d="M198,740 V647 A85,85 0 0 1 368,647 V740 Z" fill="var(--tag-yellow)" stroke="var(--forest)" stroke-width="3"/>
      <circle cx="285" cy="568" r="9" fill="var(--leaf-light)" stroke="var(--forest)" stroke-width="3"/>
      <text class="display" x="284" y="597" text-anchor="middle" font-size="23" fill="var(--ink)">Small Box</text>
      <text class="display" x="284" y="629" text-anchor="middle" font-size="23" fill="var(--ink)">for</text>
      <text class="display" x="284" y="661" text-anchor="middle" font-size="23" fill="var(--ink)">£7.50</text>
    </g>
    <g class="price-tag tag-medium">
      <path d="M448,760 V588 A104,104 0 0 1 656,588 V760 Z" fill="var(--tag-yellow)" stroke="var(--forest)" stroke-width="3"/>
      <circle cx="551" cy="512" r="9" fill="var(--leaf-light)" stroke="var(--forest)" stroke-width="3"/>
      <text class="display" x="552" y="560" text-anchor="middle" font-size="23" fill="var(--ink)">Medium Box</text>
      <text class="display" x="552" y="594" text-anchor="middle" font-size="23" fill="var(--ink)">for</text>
      <text class="display" x="552" y="628" text-anchor="middle" font-size="23" fill="var(--ink)">£13.00</text>
    </g>
    <g class="price-tag tag-large">
      <path d="M744,770 V518 A128,128 0 0 1 1000,518 V770 Z" fill="var(--tag-yellow)" stroke="var(--forest)" stroke-width="3"/>
      <circle cx="871" cy="412" r="10" fill="var(--leaf-light)" stroke="var(--forest)" stroke-width="3"/>
      <text class="display" x="872" y="477" text-anchor="middle" font-size="23" fill="var(--ink)">Large Box</text>
      <text class="display" x="872" y="527" text-anchor="middle" font-size="23" fill="var(--ink)">for</text>
      <text class="display" x="872" y="575" text-anchor="middle" font-size="23" fill="var(--ink)">£18.50</text>
    </g>

    <!-- produce box illustrations -->
    <rect class="produce-illustration" role="img" aria-label="Small cardboard delivery box filled with fruit and vegetables" x="175" y="680" width="203" height="112" rx="4" fill="url(#produce-box)"/>
    <rect class="produce-illustration" role="img" aria-label="Medium cardboard delivery box filled with fruit and vegetables" x="410" y="650" width="255" height="142" rx="4" fill="url(#produce-box)"/>
    <rect class="produce-illustration" role="img" aria-label="Large cardboard delivery box filled with fruit and vegetables" x="690" y="610" width="328" height="182" rx="4" fill="url(#produce-box)"/>

    <!-- free badge -->
    <g class="free-badge" transform="translate(236,525) rotate(-12)">
      <polygon fill="var(--badge-red)" stroke="var(--white)" stroke-width="2"
        points="-44,0 -36,-8 -42,-16 -30,-18 -28,-28 -16,-24 -8,-32 0,-24 8,-32 16,-24 28,-28 30,-18 42,-16 36,-8 44,0 36,8 42,16 30,18 28,28 16,24 8,32 0,24 -8,32 -16,24 -28,28 -30,18 -42,16 -36,8"/>
      <text class="body-copy" x="0" y="8" text-anchor="middle" font-size="21" font-weight="600" fill="var(--white)">FREE</text>
    </g>

    <!-- box types band -->
    <g class="box-types">
      <rect x="165" y="811" width="870" height="71" fill="var(--forest)"/>
      <text class="body-copy" x="600" y="837" text-anchor="middle" font-size="18" font-weight="600" fill="var(--gold)">Three box types apply to each size box</text>
      <text class="body-copy" x="600" y="872" text-anchor="middle" font-size="20" font-weight="600" fill="var(--gold)" xml:space="preserve">•  Fruit Only      •  Mixed Fruit and Vegetables      •  Vegetables Only</text>
    </g>

    <text class="body-copy delivery-note" x="165" y="906" font-size="14" fill="var(--ink)">Your box is left on your doorstep before 5am so you can bring it in before you leave for work / school run etc..</text>
  </svg>
</body>
</html>
```